依頼詳細
種の袋を陳列棚に並べて販売しております。他社の種の販売もされている中で自社の種の袋が目立ち最新のデザインでお客様の目を引くようなものをデザインしていただければと思います。
記載項目
サイズ:W9.8mm×H15.6mm 印刷/両面カラー
希望イメージ
シンプル 複雑
単色 カラフル
暗い 明るい
日常 高級
遊び心 厳粛
未来的 伝統的
女性的 男性的
希望する色
赤系、黄・オレンジ系
納品ファイル
• イラストレーター形式 (.ai)
• フォトショップ形式 (.psd)
補足説明
パワーポイントデータにデザイン指示書があります。
現在のパッケージも添付します。
陳列棚のイメージも添付します。
ハヤセミドリにもデザインが並ぶかもしれませんので素晴らしいデザインをお願いします。
依頼公開後の追記内容
北浜青果園ホームページ

http://www.kitahama-seika.example.jp/
表面の商品名(ほうれん草)は、上から4.5センチ以内にデザインをお願いします。
(陳列棚に並べたときに見えるように)

料金の表示枠もデザインに入れてください。
左から1センチ上から5.9センチのところから白枠を付けてください。
白枠はW1.7×1センチ 角丸

詳細が遅くなりすみません。よろしくお願いします。
■ 選んだ理由

今までの概念にないデザインをしていただきありがとうございました。某有名ドラックストアにてこのデザインの種を販売する予定です。楽しみにお待ちください。お客様がとても喜んでおりました。今後他の種類の野菜もデザインを増やしていく予定ですのでその際は宜しくお願いします。

■ 提案者全員のお礼・コメント

複数のデザインありがとうございました。今後もコンペを行っていきますのでよろしくお願いします。

```html
<!DOCTYPE html>
<html lang="ja">
<head>
<meta charset="utf-8">
<title>ほうれん草 種袋</title>
<link href="https://fonts.googleapis.com/css2?family=Noto+Serif+JP:wght@500;700;900&family=Noto+Sans+JP:wght@400;500;700&display=swap" rel="stylesheet">
<style>
  :root {
    --bg-top: #ffffff;
    --bg-bottom: #e4e4e2;
    --ribbon-dark: #6b3f17;
    --ribbon-mid: #9a6530;
    --ribbon-light: #c8975a;
    --title-brown: #4a2a12;
    --leaf-dark: #2f6b1e;
    --leaf-mid: #5c9c34;
    --leaf-light: #a6cf6a;
    --stem-pink: #d9a0a0;
    --orange: #f39800;
    --green: #8bbf3c;
    --text: #3a2a1a;
    --white: #ffffff;
  }
  * { margin: 0; padding: 0; box-sizing: border-box; }
  html, body { width: 813px; height: 1200px; overflow: hidden; background: #ffffff; }
  .packet {
    position: relative;
    width: 813px;
    height: 1200px;
    background: linear-gradient(180deg, var(--bg-top) 0%, #f4f4f2 55%, var(--bg-bottom) 100%);
    overflow: hidden;
    font-family: "Noto Sans JP", sans-serif;
    color: var(--text);
  }
  .maker-ribbon { position: absolute; left: 60px; top: 26px; width: 693px; height: 120px; }
  .maker-ribbon__label {
    position: absolute; left: 0; top: 24px; width: 693px; text-align: center;
    font-family: "Noto Serif JP", serif; font-weight: 700; font-size: 50px;
    color: var(--white); letter-spacing: 4px; line-height: 64px;
  }
  .category {
    position: absolute; left: 0; top: 150px; width: 813px; text-align: center;
    font-family: "Noto Serif JP", serif; font-weight: 700; font-size: 28px;
    color: var(--title-brown); letter-spacing: 4px;
  }
  .product-name {
    position: absolute; left: 0; top: 168px; width: 813px; text-align: center;
    font-family: "Noto Serif JP", serif; font-weight: 900; font-size: 104px;
    color: var(--title-brown); letter-spacing: 2px; line-height: 150px;
  }
  .rule { position: absolute; left: 256px; top: 318px; width: 300px; height: 4px; }
  .produce-photo {
    position: absolute; left: 70px; top: 335px; width: 640px; height: 600px;
    border-radius: 48% 40% 30% 36% / 44% 42% 30% 30%;
    background:
      radial-gradient(ellipse at 20% 85%, var(--stem-pink) 0%, rgba(217,160,160,0) 22%),
      radial-gradient(ellipse at 55% 40%, var(--leaf-light) 0%, var(--leaf-mid) 45%, var(--leaf-dark) 100%);
  }
  .price-box {
    position: absolute; left: 506px; top: 500px; width: 134px; height: 66px;
    background: var(--white); border-radius: 10px;
  }
  .badge {
    position: absolute; top: 950px; height: 120px; border-radius: 8px;
    color: var(--white); text-align: center;
  }
  .badge--planter { left: 198px; width: 106px; background: var(--orange); }
  .badge--season { left: 316px; width: 100px; background: var(--green); }
  .badge__icon { display: block; margin: 14px auto 0; }
  .badge__caption {
    position: absolute; left: 0; bottom: 8px; width: 100%;
    font-size: 17px; font-weight: 700; line-height: 20px;
  }
  .badge--planter .badge__caption {
    bottom: 0; height: 34px; line-height: 34px; background: var(--white);
    color: var(--orange); border: 3px solid var(--orange); border-radius: 0 0 8px 8px; font-size: 16px;
  }
  .badge__season-name { position: absolute; left: 56px; top: 14px; font-size: 26px; font-weight: 700; line-height: 28px; }
  .badge__season-sub { position: absolute; left: 60px; top: 42px; font-size: 16px; font-weight: 700; }
  .description {
    position: absolute; left: 430px; top: 952px; width: 346px;
    font-size: 23px; line-height: 32px; font-weight: 500; color: var(--text);
  }
  .company {
    position: absolute; left: 0; top: 1108px; width: 813px;
    display: flex; align-items: center; justify-content: center; gap: 14px;
  }
  .company__dot { width: 44px; height: 44px; border-radius: 50%; background: #e53a2a; }
  .company__name {
    font-family: "Noto Sans JP", sans-serif; font-weight: 700; font-size: 36px;
    color: var(--text); letter-spacing: 2px;
  }
</style>
</head>
<body>
<div class="packet">
  <svg class="maker-ribbon" viewBox="0 0 693 120" aria-hidden="true">
    <defs>
      <linearGradient id="ribbonFill" x1="0" y1="0" x2="0" y2="1">
        <stop offset="0" stop-color="#b07a3e"/>
        <stop offset="0.5" stop-color="#8a5423"/>
        <stop offset="1" stop-color="#5e3512"/>
      </linearGradient>
    </defs>
    <polygon points="0,30 70,30 70,104 0,104 22,67" fill="#5a3210"/>
    <polygon points="693,30 623,30 623,104 693,104 671,67" fill="#5a3210"/>
    <polygon points="48,104 70,118 70,104" fill="#3a1e08"/>
    <polygon points="645,104 623,118 623,104" fill="#3a1e08"/>
    <rect x="48" y="10" width="597" height="94" fill="url(#ribbonFill)"/>
    <rect x="56" y="16" width="581" height="82" fill="none" stroke="#d8b07a" stroke-width="2"/>
  </svg>
  <div class="maker-ribbon__label" style="left:60px;top:50px;width:693px;position:absolute;">北浜青果園謹製</div>

  <div class="category">・野菜の種・</div>
  <h1 class="product-name">ほうれん草</h1>
  <svg class="rule" viewBox="0 0 300 4" aria-hidden="true"><rect width="300" height="3" fill="#4a2a12"/></svg>

  <div class="produce-photo" role="img" aria-label="収穫したほうれん草の束の写真"></div>
  <div class="price-box" aria-label="価格表示欄"></div>

  <div class="badge badge--planter">
    <svg class="badge__icon" width="56" height="48" viewBox="0 0 56 48" aria-hidden="true">
      <rect x="2" y="6" width="52" height="8" rx="2" fill="#fff"/>
      <path d="M8 14 H48 L44 44 H12 Z" fill="#fff"/>
    </svg>
    <div class="badge__caption">プランター可</div>
  </div>

  <div class="badge badge--season">
    <svg style="position:absolute;left:14px;top:14px" width="40" height="52" viewBox="0 0 40 52" aria-hidden="true">
      <path d="M20 50 V22" stroke="#fff" stroke-width="4" fill="none"/>
      <path d="M20 24 C8 24 2 14 4 4 C14 4 20 12 20 24 Z" fill="#fff"/>
      <path d="M20 26 C30 26 38 18 36 8 C26 8 20 16 20 26 Z" fill="#fff"/>
    </svg>
    <span class="badge__season-name">秋</span>
    <span class="badge__season-sub">まき</span>
    <div class="badge__caption">15～20℃</div>
  </div>

  <p class="description">プランターでも栽培可能。葉ものの秋まき野菜は冬の霜に当たることで、葉が柔らかく味も甘みがある野菜になります。</p>

  <div class="company">
    <span class="company__dot" aria-hidden="true"></span>
    <span class="company__name">株式会社 北浜青果園</span>
  </div>
</div>
</body>
</html>
```